Bright Tooth Dentistry Business Card

We need business cards for our dental office.
We are looking for a clean, elegant design

We provide dental services to children.
Our card needs to be appealing to referring dentists, parents and our team

Target Market(s)

referring dentists, parents and our team

Industry/Entity Type

Dental Clinic

Contact Information for Business Card

4816 Juniper Lane, Suite 240
Cedar Hollow, PA 15237

412-837-2961 Voice
412-837-2962 fax
info@brighttoothdentalpa.com email
www.brighttoothdentalpa.com web

Font styles to use
Sans Serif

Requirements
Must have
• White background - clean, crisp, elegant, simple
• rounded corners
• different color palate - once we come up with design, we will replace the blue with orange, green,
Nice to have
• Follow our logo typeface and colors
• then we can replace color

```html
<!DOCTYPE html>
<html lang="en">
<head>
<meta charset="utf-8">
<title>Bright Tooth Dentistry – Business Card</title>
<link href="https://fonts.googleapis.com/css2?family=Quicksand:wght@400;500;700&display=swap" rel="stylesheet">
<style>
  :root {
    --brand: #1aa9e6;
    --ink: #5f5f5f;
    --card-edge: #3a3a3a;
    --page: #ffffff;
  }
  html, body {
    margin: 0;
    padding: 0;
    width: 1200px;
    height: 1200px;
    overflow: hidden;
    background: var(--page);
    font-family: "Quicksand", sans-serif;
  }
  .canvas {
    position: relative;
    width: 1200px;
    height: 1200px;
  }
  .card {
    position: absolute;
    width: 512px;
    height: 292px;
    border: 1.2px solid var(--card-edge);
    border-radius: 14px;
    background: var(--page);
    box-sizing: border-box;
  }
  .card--front { left: 360px; top: 282px; }
  .card--back  { left: 356px; top: 589px; }

  .brand-dot {
    position: absolute;
    border-radius: 50%;
    background: var(--brand);
  }
  .card--front .brand-dot {
    width: 84px; height: 84px;
    left: 212px; top: 70px;
  }
  .card--back .brand-dot {
    width: 76px; height: 76px;
    left: 104px; top: 105px;
  }
  .brand-name {
    position: absolute;
    margin: 0;
    color: var(--brand);
    font-weight: 700;
    white-space: nowrap;
    transform: translateX(-50%);
  }
  .card--front .brand-name {
    left: 256px; top: 200px;
    font-size: 26px;
  }
  .card--back .brand-name {
    left: 374px; top: 57px;
    font-size: 18.5px;
  }

  .address {
    position: absolute;
    left: 374px; top: 98px;
    transform: translateX(-50%);
    margin: 0;
    font-style: normal;
    text-align: center;
    font-size: 10px;
    line-height: 14px;
    letter-spacing: 0.08em;
    text-transform: uppercase;
    color: var(--ink);
    white-space: nowrap;
  }

  .contact-block {
    position: absolute;
    left: 286px; top: 166px;
    width: 176px; height: 78px;
    border-left: 2.4px solid var(--brand);
    border-right: 2.4px solid var(--brand);
    box-sizing: border-box;
  }
  .phones {
    position: absolute;
    left: 28px; top: 6px;
    margin: 0;
    font-size: 10px;
    line-height: 14px;
    letter-spacing: 0.1em;
    color: var(--ink);
    white-space: nowrap;
  }
  .phones dt { display: inline-block; width: 30px; margin: 0; text-transform: uppercase; }
  .phones dd { display: inline; margin: 0; }
  .phones div { display: block; }
  .web {
    position: absolute;
    left: 50%; top: 50px;
    transform: translateX(-50%);
    margin: 0;
    text-align: center;
    font-size: 7px;
    line-height: 11px;
    letter-spacing: 0.04em;
    text-transform: uppercase;
    color: var(--ink);
    white-space: nowrap;
  }
</style>
</head>
<body>
<main class="canvas">

  <section class="card card--front" aria-label="Card front">
    <span class="brand-dot" aria-hidden="true"></span>
    <h1 class="brand-name">Bright Tooth Dentistry</h1>
  </section>

  <section class="card card--back" aria-label="Card back">
    <span class="brand-dot" aria-hidden="true"></span>
    <h2 class="brand-name">Bright Tooth Dentistry</h2>
    <address class="address">
      4816 Juniper Lane, Suite 240<br>
      Cedar Hollow, PA 15237
    </address>
    <div class="contact-block">
      <dl class="phones">
        <div><dt>Fax</dt><dd>412 - 837 - 2961</dd></div>
        <div><dt>Tel</dt><dd>412 - 837 - 2962</dd></div>
      </dl>
      <p class="web">
        info@brighttoothdentalpa.com<br>
        www.brighttoothdentalpa.com
      </p>
    </div>
  </section>

</main>
</body>
</html>
```